nestlybloom - Ballon Design

I need a Ballon designed. Please use the psb file ballon_template.psb as template.

I would like to have a ballon designed similar to the file "example.png".
instead of the lorna kin logo please use my attached logo "nestlybloom logo.ai"

The text should be the same " IT'S A MOM" but the logo should be different.

I should look like more elegant. should be also white background. But for the design feel free.

thanks.
Updates

Please also add the webpage "www.nestlybloom.eu" on the ballon design.

```html
<!DOCTYPE html>
<html lang="en">
<head>
<meta charset="utf-8">
<title>nestlybloom – It's a Mom balloon</title>
<link href="https://fonts.googleapis.com/css2?family=Abril+Fatface&family=Nunito+Sans:wght@800&display=swap" rel="stylesheet">
<style>
  :root {
    --backdrop: #fde2b1;
    --balloon-white: #f7f6f1;
    --navy: #1c2f5e;
    --berry: #8c2041;
    --berry-soft: #b04a63;
    --brand-pink: #c9667e;
    --leaf-green: #9fd1b4;
    --petal-coral: #f0a28d;
    --ink: #2a2a2a;
  }
  html, body {
    margin: 0;
    width: 1200px;
    height: 1139px;
    overflow: hidden;
    background: var(--backdrop);
  }
  .canvas {
    position: relative;
    width: 1200px;
    height: 1139px;
  }
  .balloon-face {
    position: absolute;
    left: 110px;
    top: 80px;
    width: 980px;
    height: 980px;
    border-radius: 50%;
    background: var(--balloon-white);
    overflow: hidden;
  }
  .floral-border {
    position: absolute;
    inset: 0;
  }
  .headline {
    position: absolute;
    left: 0;
    width: 100%;
    margin: 0;
    text-align: center;
    font-family: "Abril Fatface", serif;
    font-weight: 400;
    line-height: 1;
    color: var(--navy);
  }
  .headline-its { top: 150px; font-size: 140px; letter-spacing: 6px; }
  .headline-a { top: 300px; font-size: 120px; }
  .headline-mom {
    top: 440px;
    font-size: 230px;
    color: var(--berry);
    display: flex;
    justify-content: center;
    align-items: center;
  }
  .heart-artwork {
    display: block;
    width: 200px;
    height: 190px;
    margin: 0 8px;
    border-radius: 24px;
    background: linear-gradient(160deg, var(--berry-soft), var(--berry));
  }
  .brand-name {
    position: absolute;
    top: 715px;
    left: 0;
    width: 100%;
    margin: 0;
    text-align: center;
    font-family: "Nunito Sans", sans-serif;
    font-weight: 800;
    font-size: 60px;
    line-height: 1;
    color: var(--brand-pink);
  }
  .brand-dot {
    position: absolute;
    top: 792px;
    left: 482px;
    width: 16px;
    height: 16px;
    border-radius: 50%;
    background: var(--brand-pink);
  }
  .web-address {
    position: absolute;
    top: 822px;
    left: 0;
    width: 100%;
    margin: 0;
    text-align: center;
    font-family: "Nunito Sans", sans-serif;
    font-weight: 800;
    font-size: 30px;
    line-height: 1;
    color: var(--ink);
  }
</style>
</head>
<body>
<main class="canvas">
  <section class="balloon-face">
    <svg class="floral-border" viewBox="0 0 980 980" role="img" aria-label="Floral border of leaves, berries and flowers around the balloon edge">
      <defs>
        <linearGradient id="borderTone" x1="0" y1="0" x2="1" y2="1">
          <stop offset="0" stop-color="#9fd1b4" stop-opacity="0.55"/>
          <stop offset="0.5" stop-color="#f0a28d" stop-opacity="0.45"/>
          <stop offset="1" stop-color="#9fd1b4" stop-opacity="0.55"/>
        </linearGradient>
      </defs>
      <circle cx="490" cy="490" r="465" fill="none" stroke="url(#borderTone)" stroke-width="50"/>
    </svg>

    <h1 class="headline headline-its">IT’S</h1>
    <p class="headline headline-a">A</p>
    <p class="headline headline-mom">
      <span>M</span>
      <span class="heart-artwork" role="img" aria-label="Heart illustration standing in for the letter O"></span>
      <span>M</span>
    </p>

    <p class="brand-name">nestlybloom</p>
    <span class="brand-dot"></span>
    <p class="web-address">www.nestlybloom.eu</p>
  </section>
</main>
</body>
</html>
```